Rework of Honey Labels - Updated for clarity

I am looking for a re-do of our current creamed honey labels.
Creamed honey is a butter-consistency. There are 5 flavors - original, lavender, chocolate, lemon, cinnamon. We want for it to look sophisticated and luxurious. We want the labels to all be cohesive in this group, but to be able to easily tell the difference between the products by color or something quick besides just words to tell the difference in the product. The product will be an off-white/light amber - except for the chocolate which is the color of Cremoso. There are three size containers for each of these honeys. But we can just focus on the single size for this contest.
The honey market in our area is extremely competitive. Right now, I feel our labels look more homemade. I want something that stands out. We charge a premium for our products. We want for our labels to look like we are a superior product. We are getting our product in many local stores and need to differentiate ourselves. I am attaching some of the labels that I think stand out. As for the labels themselves. They can include that whole blurb about us as Brookvale Meadow - or not. It is not truly necessary to have on the labels. But the logo needs to be included.
For all of these, we want something unique and special. Like you are going for an English mid-day tea at an upscale hotel in London with the Queen (well, I guess now the King...but really I think of the Queen).
I am uploading our current labels and then a few labels to take inspiration from.
Updates
I just reworked the description to be more limited in what I was asking for. Looking for a label for creamed honey in one size jar only. Thank you.

```html
<!DOCTYPE html>
<html lang="en">
<head>
<meta charset="utf-8">
<title>Creamed Honey Label Range</title>
<link href="https://fonts.googleapis.com/css2?family=Fraunces:opsz,wght@9..144,700&family=Lora:wght@400;500;600&family=Yellowtail&display=swap" rel="stylesheet">
<style>
  :root {
    --bg: #efefef;
    --label: #141414;
    --cream: #efe9d8;
    --gold: #c8b98f;
    --original: #d9982a;
    --chocolate: #a27b4b;
    --lavender: #6b4c9c;
    --lemon: #e6c31c;
    --cinnamon: #c9a35c;
  }
  * { margin: 0; padding: 0; box-sizing: border-box; }
  html, body { width: 1200px; height: 1200px; overflow: hidden; background: var(--bg); }
  .label-range {
    position: absolute; left: 45px; top: 440px;
    display: flex; gap: 40px;
  }
  .label {
    width: 190px; height: 320px;
    background: radial-gradient(ellipse at 70% 30%, #3a3a3a 0%, var(--label) 60%);
    border-radius: 70px 70px 14px 14px / 46px 46px 14px 14px;
    padding: 8px;
  }
  .label-frame {
    width: 100%; height: 100%;
    border: 1.5px solid var(--gold);
    border-radius: 64px 64px 10px 10px / 40px 40px 10px 10px;
    display: flex; flex-direction: column; align-items: center;
    padding-top: 26px;
    color: var(--cream);
    text-align: center;
  }
  .brand-mark {
    display: flex; flex-direction: column; align-items: center; justify-content: center;
    gap: 8px; height: 76px;
  }
  .brand-name {
    font-family: "Lora", serif; font-weight: 600; font-size: 12px;
    color: var(--gold); letter-spacing: 0.06em; line-height: 1.3;
    white-space: nowrap;
  }
  .flavour-bar { width: 54px; height: 3px; background: var(--accent); }
  .product-type {
    font-family: "Lora", serif; font-weight: 600; font-size: 12px;
    letter-spacing: 0.14em; margin-top: 12px;
  }
  .product-name {
    font-family: "Fraunces", serif; font-weight: 700; font-size: 48px;
    line-height: 1; margin-top: -1px; letter-spacing: -0.01em;
  }
  .bee-emblem {
    width: 28px; height: 13px; margin-top: 10px;
    background: var(--gold); border-radius: 50%; opacity: 0.85;
  }
  .purity { font-family: "Lora", serif; font-size: 9.5px; letter-spacing: 0.12em; margin-top: 6px; }
  .flavour {
    font-family: "Yellowtail", "Brush Script MT", cursive; font-size: 24px; color: var(--accent);
    margin-top: 2px; line-height: 1.15;
  }
  .grade { font-family: "Lora", serif; font-size: 7.5px; letter-spacing: 0.1em; margin-top: 2px; }
  .rule { width: 78px; height: 1px; background: var(--cream); margin: 5px 0; }
  .net-weight { font-family: "Lora", serif; font-size: 6.5px; }
  .original { --accent: var(--original); }
  .chocolate { --accent: var(--chocolate); }
  .lavender { --accent: var(--lavender); }
  .lemon { --accent: var(--lemon); }
  .cinnamon { --accent: var(--cinnamon); }
</style>
</head>
<body>
<main class="label-range">
  <article class="label original">
    <div class="label-frame">
      <div class="brand-mark"><span class="brand-name">Larkspur Hollow</span><span class="flavour-bar"></span></div>
      <p class="product-type">CREAMED</p>
      <h1 class="product-name">honey</h1>
      <div class="bee-emblem" role="img" aria-label="Small gold bee emblem"></div>
      <p class="purity">100% PURE</p>
      <p class="flavour">Original</p>
      <p class="grade">US GRADE A FANCY</p>
      <span class="rule"></span>
      <p class="net-weight">Net.wt. 12 oz / 340 g</p>
    </div>
  </article>
  <article class="label chocolate">
    <div class="label-frame">
      <div class="brand-mark"><span class="brand-name">Larkspur Hollow</span><span class="flavour-bar"></span></div>
      <p class="product-type">CREAMED</p>
      <h1 class="product-name">honey</h1>
      <div class="bee-emblem" role="img" aria-label="Small gold bee emblem"></div>
      <p class="purity">100% PURE</p>
      <p class="flavour">Chocolate</p>
      <p class="grade">US GRADE A FANCY</p>
      <span class="rule"></span>
      <p class="net-weight">Net.wt. 12 oz / 340 g</p>
    </div>
  </article>
  <article class="label lavender">
    <div class="label-frame">
      <div class="brand-mark"><span class="brand-name">Larkspur Hollow</span><span class="flavour-bar"></span></div>
      <p class="product-type">CREAMED</p>
      <h1 class="product-name">honey</h1>
      <div class="bee-emblem" role="img" aria-label="Small gold bee emblem"></div>
      <p class="purity">100% PURE</p>
      <p class="flavour">Lavender</p>
      <p class="grade">US GRADE A FANCY</p>
      <span class="rule"></span>
      <p class="net-weight">Net.wt. 12 oz / 340 g</p>
    </div>
  </article>
  <article class="label lemon">
    <div class="label-frame">
      <div class="brand-mark"><span class="brand-name">Larkspur Hollow</span><span class="flavour-bar"></span></div>
      <p class="product-type">CREAMED</p>
      <h1 class="product-name">honey</h1>
      <div class="bee-emblem" role="img" aria-label="Small gold bee emblem"></div>
      <p class="purity">100% PURE</p>
      <p class="flavour">Lemon</p>
      <p class="grade">US GRADE A FANCY</p>
      <span class="rule"></span>
      <p class="net-weight">Net.wt. 12 oz / 340 g</p>
    </div>
  </article>
  <article class="label cinnamon">
    <div class="label-frame">
      <div class="brand-mark"><span class="brand-name">Larkspur Hollow</span><span class="flavour-bar"></span></div>
      <p class="product-type">CREAMED</p>
      <h1 class="product-name">honey</h1>
      <div class="bee-emblem" role="img" aria-label="Small gold bee emblem"></div>
      <p class="purity">100% PURE</p>
      <p class="flavour">Cinnamon</p>
      <p class="grade">US GRADE A FANCY</p>
      <span class="rule"></span>
      <p class="net-weight">Net.wt. 12 oz / 340 g</p>
    </div>
  </article>
</main>
</body>
</html>
```